Laser Open House

We need a postcard to announce a Dorvana Radio Frequency open house. This will be held on August 30th from 5-8.
There will be a $35 admission fee that will be charged at the time of reservation to assure a spot. There will be live demos, beverages and food available. For the $35, each attendee will receive a choice of a mini-massage or a skin care kit which includes a cleanser, moisturizer and sunscreen.

```html
<!DOCTYPE html>
<html lang="en">
<head>
<meta charset="utf-8">
<title>Dorvana Radio Frequency Open House Postcard</title>
<link href="https://fonts.googleapis.com/css2?family=Oswald:wght@400;500;600;700&family=Open+Sans:wght@400;600;700&display=swap" rel="stylesheet">
<style>
  :root {
    --navy: #1d3c78;
    --blue: #2b6cb8;
    --blue-light: #4a8fd6;
    --teal: #36bcc6;
    --teal-light: #94dfe4;
    --white: #ffffff;
    --paper: #fdfdfd;
    --stage: #e9ecee;
    --stamp: #cfd3d6;
    --skin-a: #f1d8c9;
    --skin-b: #d9b3a0;
  }
  * { box-sizing: border-box; margin: 0; padding: 0; }
  html, body { width: 900px; height: 1200px; overflow: hidden; }
  body { background: var(--stage); font-family: "Open Sans", Arial, sans-serif; position: relative; }

  .postcard {
    position: absolute; left: 40px; width: 820px; height: 540px;
    background: var(--paper); overflow: hidden;
    box-shadow: 0 6px 18px rgba(0,0,0,.18);
  }
  .postcard--front { top: 30px; }
  .postcard--back { top: 630px; }
  .shapes { position: absolute; inset: 0; }
  .abs { position: absolute; }

  .title { font-family: "Oswald", Arial, sans-serif; text-transform: uppercase; line-height: 1.05; }
  .title__main { font-weight: 700; font-size: 46px; color: var(--navy); }
  .title__sub { font-weight: 500; font-size: 34px; color: var(--blue); }
  .postcard--back .title__main, .postcard--back .title__sub { color: var(--white); }

  .photo { position: absolute; }
  .photo--eye { right: 0; top: 0; width: 450px; height: 235px;
    background: linear-gradient(100deg, #ffffff 0%, var(--skin-a) 30%, var(--skin-b) 100%); }
  .photo--portrait { left: 0; top: 115px; width: 340px; height: 330px;
    background: linear-gradient(160deg, #ffffff 0%, var(--skin-a) 45%, #9a6a52 100%); }

  .price-badge {
    position: absolute; border-radius: 50%; background: var(--teal);
    border: 6px solid var(--white); box-shadow: 0 0 0 4px var(--teal-light);
    color: var(--white); text-align: center;
    display: flex; flex-direction: column; justify-content: center; align-items: center;
  }
  .price-badge__amount { font-family: "Oswald", Arial, sans-serif; font-weight: 600; font-size: 70px; line-height: 1; }
  .price-badge__label { font-family: "Oswald", Arial, sans-serif; font-size: 15px; letter-spacing: 1px; text-transform: uppercase; margin-top: 4px; }

  .date-bar { right: 0; top: 214px; width: 360px; height: 48px; background: var(--teal);
    border-radius: 24px 0 0 24px; color: var(--white);
    font-family: "Oswald", Arial, sans-serif; font-size: 27px; line-height: 48px; padding-left: 36px; }

  .offer { left: 400px; top: 278px; }
  .offer__head { font-family: "Oswald", Arial, sans-serif; font-weight: 700; font-size: 31px; line-height: 1.05; color: var(--navy); text-transform: uppercase; }
  .offer__note { font-size: 13px; color: var(--blue); margin-top: 4px; }

  .perks { left: 42px; top: 370px; list-style: none; }
  .perks li { font-size: 22px; color: var(--navy); line-height: 1.45; padding-left: 24px; position: relative; }
  .perks li::before { content: ""; position: absolute; left: 0; top: 12px; width: 11px; height: 11px; border-radius: 50%; background: var(--teal); }

  .thumb { position: absolute; top: 384px; width: 110px; height: 110px; border-radius: 50%;
    border: 5px solid var(--white); box-shadow: 0 0 0 3px var(--teal);
    background: radial-gradient(circle at 45% 40%, var(--skin-a), var(--skin-b)); }

  .stamp { right: 40px; top: 135px; width: 84px; height: 92px; background: var(--stamp); }

  .event-bar { left: 0; top: 432px; width: 450px; height: 78px; background: var(--navy);
    border-radius: 0 40px 0 0; padding: 8px 0 0 30px; }
  .event-bar__name { font-family: "Oswald", Arial, sans-serif; font-size: 28px; color: var(--teal-light); line-height: 1.2; }
  .event-bar__url { font-size: 19px; color: var(--white); }
</style>
</head>
<body>

<section class="postcard postcard--front" aria-label="Postcard front">
  <div class="photo photo--eye" role="img" aria-label="Close-up photo of a woman's eye and smooth skin"></div>
  <svg class="shapes" viewBox="0 0 820 540" aria-hidden="true">
    <path d="M0,280 C260,240 520,220 820,196 L820,212 C520,236 260,258 0,300 Z" fill="var(--teal-light)"/>
    <path d="M0,300 C260,258 520,236 820,212 L820,268 C520,276 260,310 0,352 Z" fill="var(--blue)"/>
    <path d="M0,352 C260,310 520,276 820,268 L820,282 C520,292 260,326 0,366 Z" fill="var(--teal)"/>
    <path d="M0,505 C300,480 560,470 820,488 L820,540 L0,540 Z" fill="var(--blue)"/>
    <path d="M0,518 C300,498 560,492 820,505 L820,540 L0,540 Z" fill="var(--teal)"/>
  </svg>

  <h1 class="title abs" style="left:28px; top:22px;">
    <span class="title__main">Dorvana Radio</span><br>
    <span class="title__sub">Frequency Open House</span>
  </h1>

  <div class="price-badge" style="left:58px; top:168px; width:184px; height:184px;">
    <span class="price-badge__amount">$35</span>
    <span class="price-badge__label">Admission Fee</span>
  </div>

  <div class="date-bar abs">August 30th from 5-8</div>

  <div class="offer abs">
    <p class="offer__head">Choose a mini-massage<br>or skin care kit for $35</p>
    <p class="offer__note">Cleanser, moisturizer and sunscreen available</p>
  </div>

  <ul class="perks abs">
    <li>Live demos</li>
    <li>Beverages and</li>
    <li>Food available</li>
  </ul>

  <div class="thumb" style="left:420px;" role="img" aria-label="Photo of an eye with long lashes"></div>
  <div class="thumb" style="left:555px;" role="img" aria-label="Photo of a woman receiving a facial treatment"></div>
  <div class="thumb" style="left:690px;" role="img" aria-label="Photo of a smiling woman touching her cheek"></div>
</section>

<section class="postcard postcard--back" aria-label="Postcard back">
  <svg class="shapes" viewBox="0 0 820 540" aria-hidden="true">
    <defs>
      <linearGradient id="headerBand" x1="0" y1="0" x2="1" y2="0">
        <stop offset="0" stop-color="var(--navy)"/>
        <stop offset="1" stop-color="var(--blue-light)"/>
      </linearGradient>
    </defs>
    <path d="M0,0 L820,0 L820,80 C560,92 300,104 0,122 Z" fill="url(#headerBand)"/>
    <path d="M0,122 C300,104 560,92 820,80 L820,92 C560,104 300,116 0,134 Z" fill="var(--teal)"/>
    <rect x="0" y="510" width="820" height="30" fill="var(--teal)"/>
  </svg>

  <h2 class="title abs" style="left:28px; top:12px;">
    <span class="title__main">Dorvana Radio</span><br>
    <span class="title__sub">Frequency Open House</span>
  </h2>

  <div class="photo photo--portrait" role="img" aria-label="Portrait photo of a woman with glowing skin"></div>

  <div class="price-badge" style="left:325px; top:180px; width:180px; height:180px;">
    <span class="price-badge__amount">$35</span>
    <span class="price-badge__label">Admission Fee</span>
  </div>

  <div class="stamp abs" aria-hidden="true"></div>

  <div class="event-bar abs">
    <p class="event-bar__name">Laser Open House</p>
    <p class="event-bar__url">www.dorvanaspa.com</p>
  </div>
</section>

</body>
</html>
```